Fernvale Accounting - New Postcard for B2B marketing

I need a postcard for my business that provides cloud-based bookkeeping services with LedgerCloud Online. Our clients are small independently owned businesses. Please use our website for inspiration (colors, content, etc)... www.FernvaleAccounting.com.

Target Market(s)

Small, independently-owned businesses, including restaurants, retail stores, small medical practices, etc

Industry/Entity Type

Bookkeeper

Font styles to use
Serif

Colors
3276b5
155ea9
c4d6e9
85cae6
33a6d7

Requirements
Must have
• Must have my logo (see attached), business contact info (see website), description of services, blue color scheme
Nice to have
• Maybe add "Prices starting at $750/mo"
Content should match info on our website
4 x 6 horizontal postcard (see attached template)

```html
<!DOCTYPE html>
<html lang="en">
<head>
<meta charset="utf-8">
<title>Fernvale Accounting – Postcard</title>
<link rel="stylesheet" href="https://fonts.googleapis.com/css2?family=Merriweather:wght@400;700;900&family=Montserrat:wght@500;600;700;800&display=swap">
<style>
  :root {
    --navy: #0f3a70;
    --blue: #155ea9;
    --mid-blue: #3276b5;
    --pale-blue: #c4d6e9;
    --sky: #85cae6;
    --cyan: #33a6d7;
    --white: #ffffff;
    --ink: #1b2a3d;
    --stage: #eef1f4;
  }
  * { box-sizing: border-box; margin: 0; padding: 0; }
  html, body {
    width: 1185px; height: 1200px; overflow: hidden;
    background: var(--stage);
  }
  .canvas { position: relative; width: 1185px; height: 1200px; }
  .card {
    position: absolute; left: 172px; width: 840px; height: 560px;
    background: var(--white); overflow: hidden;
    box-shadow: 0 6px 22px rgba(15, 58, 112, 0.18);
  }
  .card--front { top: 30px; }
  .card--back { top: 610px; }
  .card svg.shapes { position: absolute; inset: 0; }
  .layer { position: absolute; }

  /* Front */
  .hero-photo {
    position: absolute; left: 300px; top: 0; width: 540px; height: 340px;
    background: linear-gradient(135deg, #f2f5f8 0%, #dde4eb 55%, #c3ced9 100%);
  }
  .headline {
    left: 38px; top: 44px; width: 420px;
    font: 900 35px/1.16 "Merriweather", serif; color: var(--white);
  }
  .price-label {
    left: 38px; top: 302px;
    font: 600 15px/1 "Montserrat", sans-serif; color: var(--white); letter-spacing: 0.5px;
  }
  .price-value {
    left: 36px; top: 322px;
    font: 800 48px/1 "Montserrat", sans-serif; color: var(--white);
  }
  .brand-name {
    display: flex; align-items: center; gap: 12px; white-space: nowrap;
    font: 700 30px/1 "Merriweather", serif; color: var(--navy);
  }
  .brand-name .brand-dot { width: 18px; height: 18px; background: var(--blue); flex: none; }
  .card--front .brand-name { left: 40px; top: 462px; }
  .contact-phone {
    left: 470px; top: 362px; display: flex; align-items: center; gap: 12px;
    font: 700 40px/1 "Montserrat", sans-serif; color: var(--white);
  }
  .contact-email {
    left: 476px; top: 426px; display: flex; align-items: center; gap: 10px;
    font: 600 19px/1 "Montserrat", sans-serif; color: var(--white);
  }
  .contact-web {
    left: 470px; top: 483px; display: flex; align-items: center; gap: 10px;
    font: 600 20px/1 "Montserrat", sans-serif; color: var(--white);
  }
  .icon { flex: none; }

  /* Back */
  .services-title {
    left: 56px; top: 60px;
    font: 500 28px/1 "Montserrat", sans-serif; color: var(--white); letter-spacing: 1px;
  }
  .service {
    left: 56px; width: 420px; display: flex; gap: 22px; align-items: flex-start;
  }
  .service--bookkeeping { top: 106px; }
  .service--reporting { top: 208px; }
  .service--payroll { top: 298px; }
  .service-icon { width: 52px; height: 52px; flex: none; margin-top: 6px; }
  .service-body { border-left: 1px solid rgba(255,255,255,0.45); padding-left: 16px; }
  .service-name {
    font: 400 14px/1.2 "Merriweather", serif; color: var(--sky);
    text-transform: uppercase; margin-bottom: 4px;
  }
  .service-text {
    font: 400 10px/1.4 "Merriweather", serif; color: var(--white);
  }
  .contact-block { left: 420px; top: 428px; width: 300px; }
  .contact-block-title {
    font: 500 22px/1 "Montserrat", sans-serif; color: var(--white); letter-spacing: 0.5px;
    padding-bottom: 8px; border-bottom: 1px solid rgba(255,255,255,0.6); margin-bottom: 10px;
  }
  .contact-line {
    display: flex; align-items: center; gap: 10px; margin-bottom: 6px;
    font: 500 15px/1.1 "Montserrat", sans-serif; color: var(--white);
  }
  .card--back .brand-name { left: 584px; top: 150px; font-size: 20px; gap: 10px; }
  .card--back .brand-name .brand-dot { width: 14px; height: 14px; }
  .stamp-box {
    left: 720px; top: 28px; width: 92px; height: 96px;
    border: 1.5px solid var(--ink);
  }
  .address-line { left: 600px; width: 210px; height: 0; border-top: 1.5px solid var(--ink); }
  .address-line--1 { top: 230px; }
  .address-line--2 { top: 276px; }
  .address-line--3 { top: 322px; }
  .partner-badge {
    left: 752px; top: 350px; width: 52px; height: 60px;
    background: var(--pale-blue); border-bottom: 8px solid var(--cyan);
  }
</style>
</head>
<body>
<main class="canvas">

  <!-- Front of postcard -->
  <section class="card card--front">
    <div class="hero-photo" role="img" aria-label="Photo of a hand typing on a laptop showing bookkeeping software beside a calculator"></div>
    <svg class="shapes" viewBox="0 0 840 560" width="840" height="560" aria-hidden="true">
      <polygon points="0,0 400,0 490,170 440,400 0,400" fill="var(--navy)"/>
      <polyline points="400,0 490,170 440,400" fill="none" stroke="var(--cyan)" stroke-width="4"/>
      <polygon points="0,290 464,290 444,380 0,380" fill="var(--blue)"/>
      <polygon points="478,340 840,340 840,560 428,560" fill="var(--blue)"/>
      <polygon points="452,340 478,340 428,560 402,560" fill="var(--navy)"/>
      <polygon points="452,470 840,470 840,522 440,522" fill="var(--cyan)"/>
    </svg>

    <h1 class="layer headline">Cloud-based Bookkeeping Services with LedgerCloud Online.</h1>
    <p class="layer price-label">PRICES STARTING AT</p>
    <p class="layer price-value">$750/m</p>

    <div class="layer brand-name"><span class="brand-dot"></span>Fernvale Accounting</div>

    <p class="layer contact-phone">
      <svg class="icon" width="30" height="30" viewBox="0 0 30 30" aria-hidden="true">
        <circle cx="15" cy="15" r="13" fill="none" stroke="#fff" stroke-width="2.5"/>
        <path d="M10 9c1-1 2-1 2.5 0l1.2 2.4c.3.6 0 1.2-.5 1.6l-.8.6c.6 1.5 1.8 2.8 3.4 3.5l.6-.8c.4-.5 1-.7 1.6-.4l2.4 1.2c.8.5.9 1.5 0 2.4-1.4 1.4-3.5 1.4-6.2-.6-2.6-2-4.6-4.7-4.6-7 0-1.2.5-2.100 1.4-2.9z" fill="#fff"/>
      </svg>
      1.877.555.0142
    </p>
    <p class="layer contact-email">
      <svg class="icon" width="22" height="16" viewBox="0 0 22 16" aria-hidden="true">
        <rect x="1" y="1" width="20" height="14" fill="none" stroke="#fff" stroke-width="1.8"/>
        <polyline points="1,1 11,9 21,1" fill="none" stroke="#fff" stroke-width="1.8"/>
      </svg>
      info@fernvaleaccounting.com
    </p>
    <p class="layer contact-web">
      <svg class="icon" width="20" height="20" viewBox="0 0 20 20" aria-hidden="true">
        <circle cx="10" cy="10" r="8.5" fill="none" stroke="#fff" stroke-width="1.8"/>
        <ellipse cx="10" cy="10" rx="3.8" ry="8.5" fill="none" stroke="#fff" stroke-width="1.5"/>
        <line x1="1.5" y1="10" x2="18.5" y2="10" stroke="#fff" stroke-width="1.5"/>
      </svg>
      www.FernvaleAccounting.com
    </p>
  </section>

  <!-- Back of postcard -->
  <section class="card card--back">
    <svg class="shapes" viewBox="0 0 840 560" width="840" height="560" aria-hidden="true">
      <circle cx="230" cy="250" r="352" fill="none" stroke="var(--cyan)" stroke-width="2"/>
      <circle cx="230" cy="250" r="335" fill="var(--navy)"/>
      <circle cx="520" cy="744" r="368" fill="var(--white)"/>
      <circle cx="520" cy="744" r="362" fill="none" stroke="var(--blue)" stroke-width="2"/>
      <circle cx="520" cy="744" r="352" fill="var(--cyan)"/>
    </svg>

    <h2 class="layer services-title">SERVICES</h2>

    <div class="layer service service--bookkeeping">
      <svg class="service-icon" viewBox="0 0 52 52" aria-hidden="true">
        <rect x="10" y="6" width="30" height="40" fill="none" stroke="#fff" stroke-width="2"/>
        <line x1="16" y1="16" x2="34" y2="16" stroke="#fff" stroke-width="2"/>
        <line x1="16" y1="24" x2="34" y2="24" stroke="#fff" stroke-width="2"/>
        <line x1="16" y1="32" x2="28" y2="32" stroke="#fff" stroke-width="2"/>
      </svg>
      <div class="service-body">
        <h3 class="service-name">Bookkeeping</h3>
        <p class="service-text">Let us take over the day to day bookkeeping so you can get back to running your business. We offer LedgerCloud Online setup and ongoing bookkeeping, including daily journal entries, accounts payables &amp; receivables, bill pay, sales tax reporting &amp; payments, account reconciliation, and more.</p>
      </div>
    </div>

    <div class="layer service service--reporting">
      <svg class="service-icon" viewBox="0 0 52 52" aria-hidden="true">
        <circle cx="24" cy="26" r="16" fill="none" stroke="#fff" stroke-width="2"/>
        <path d="M24 26V10A16 16 0 0 1 40 26z" fill="#fff"/>
      </svg>
      <div class="service-body">
        <h3 class="service-name">Financial Reporting</h3>
        <p class="service-text">We'll provide easy to understand financial reports that allow you and your team to manage cash flow, create budgets and make forecasting decisions. Want real time data? Let us provide solutions with the latest in mobile apps and dashboards.</p>
      </div>
    </div>

    <div class="layer service service--payroll">
      <svg class="service-icon" viewBox="0 0 52 52" aria-hidden="true">
        <rect x="10" y="6" width="32" height="40" rx="3" fill="none" stroke="#fff" stroke-width="2"/>
        <rect x="15" y="11" width="22" height="9" fill="none" stroke="#fff" stroke-width="2"/>
        <rect x="15" y="25" width="5" height="5" fill="#fff"/>
        <rect x="24" y="25" width="5" height="5" fill="#fff"/>
        <rect x="32" y="25" width="5" height="5" fill="#fff"/>
        <rect x="15" y="34" width="5" height="5" fill="#fff"/>
        <rect x="24" y="34" width="5" height="5" fill="#fff"/>
        <rect x="32" y="34" width="5" height="5" fill="#fff"/>
      </svg>
      <div class="service-body">
        <h3 class="service-name">Payroll Processing</h3>
        <p class="service-text">Whether you have 5 employees or 100+, payroll can be an overwhelming and time consuming task. We offer full service payroll processing, including employee on boarding and reporting.</p>
      </div>
    </div>

    <div class="layer contact-block">
      <h2 class="contact-block-title">CONTACT INFO</h2>
      <p class="contact-line">
        <svg class="icon" width="16" height="12" viewBox="0 0 22 16" aria-hidden="true">
          <rect x="1" y="1" width="20" height="14" fill="none" stroke="#fff" stroke-width="2"/>
          <polyline points="1,1 11,9 21,1" fill="none" stroke="#fff" stroke-width="2"/>
        </svg>
        info@fernvaleaccounting.com
      </p>
      <p class="contact-line">
        <svg class="icon" width="16" height="16" viewBox="0 0 30 30" aria-hidden="true">
          <circle cx="15" cy="15" r="13" fill="none" stroke="#fff" stroke-width="3"/>
          <path d="M10 9c1-1 2-1 2.5 0l1.2 2.4c.3.6 0 1.2-.5 1.6l-.8.6c.6 1.5 1.8 2.8 3.4 3.5l.6-.8c.4-.5 1-.7 1.6-.4l2.4 1.2c.8.5.9 1.5 0 2.4-1.4 1.4-3.5 1.4-6.2-.6-2.6-2-4.6-4.7-4.6-7 0-1.2.5-2.1 1.4-2.9z" fill="#fff"/>
        </svg>
        1.877.555.0142
      </p>
      <p class="contact-line">
        <svg class="icon" width="16" height="16" viewBox="0 0 20 20" aria-hidden="true">
          <circle cx="10" cy="10" r="8.5" fill="none" stroke="#fff" stroke-width="1.8"/>
          <ellipse cx="10" cy="10" rx="3.8" ry="8.5" fill="none" stroke="#fff" stroke-width="1.5"/>
          <line x1="1.5" y1="10" x2="18.5" y2="10" stroke="#fff" stroke-width="1.5"/>
        </svg>
        www.fernvaleaccounting.com
      </p>
    </div>

    <div class="layer stamp-box"></div>
    <div class="layer brand-name"><span class="brand-dot"></span>Fernvale Accounting</div>
    <div class="layer address-line address-line--1"></div>
    <div class="layer address-line address-line--2"></div>
    <div class="layer address-line address-line--3"></div>
    <div class="layer partner-badge" role="img" aria-label="Certified partner badge"></div>
  </section>

</main>
</body>
</html>
```